KT Crewing business card

Require business card which includes:
Company name: KT CREWING PTY LTD
Email: Mick@ktcrewing.com.au
Phone: 0431 556 208
ACN: 517 238 649

slogan: Onsite Auto Electrician Labour hire

Details and logo on top side
Logo only on bottom side

colour codes : #F15A29 , #939598

Target Market(s)

Western Australia mining sector

Industry/Entity Type

Mining

Contact Information for Business Card

Require business card which includes: Company name: KT CREWING PTY LTD Email: Mick@ktcrewing.com.au Phone: 0431 556 208 ACN: 517 238 649 slogan: Onsite Auto Electrician Labour hire Details and logo on top side Logo only on bottom side colour codes : #F15A29 , #939598

Colors
EE7325
F08F49
F5BC92
FAE3D3
FDF4ED

Requirements
Must have
• double sided

```html
<!DOCTYPE html>
<html lang="en">
<head>
<meta charset="utf-8">
<title>KT Crewing Business Card</title>
<link rel="stylesheet" href="https://fonts.googleapis.com/css2?family=Montserrat:wght@400;500;700&family=Orbitron:wght@600&display=swap">
<style>
  :root {
    --orange: #F15A29;
    --grey: #939598;
    --card: #1d1d1e;
    --page: #3a3a3b;
    --page-edge: #1f1f20;
    --white: #f4f4f4;
  }
  * { box-sizing: border-box; margin: 0; padding: 0; }
  html, body { width: 1200px; height: 900px; overflow: hidden; }
  body {
    background: radial-gradient(ellipse at 50% 45%, var(--page) 0%, var(--page-edge) 100%);
    font-family: "Montserrat", Arial, sans-serif;
    position: relative;
  }
  .card {
    position: absolute;
    top: 150px;
    width: 360px;
    height: 600px;
    background: var(--card);
    box-shadow: 0 18px 40px rgba(0,0,0,.55);
    overflow: hidden;
  }
  .card--front { left: 190px; }
  .card--back { left: 650px; }

  .front__company {
    position: absolute;
    top: 46px; left: 0; right: 0;
    text-align: center;
    font-family: "Orbitron", "Montserrat", sans-serif;
    font-weight: 600;
    font-size: 25px;
    color: var(--orange);
    letter-spacing: .5px;
  }
  .front__details {
    position: absolute;
    top: 190px; left: 0; right: 0;
    text-align: center;
  }
  .person__name {
    font-weight: 700;
    font-size: 24px;
    color: var(--orange);
    letter-spacing: .5px;
  }
  .person__role {
    font-size: 15px;
    color: var(--white);
    letter-spacing: 1px;
    margin-top: 2px;
  }
  .person__dash {
    width: 16px; height: 2px;
    background: var(--orange);
    margin: 12px auto;
  }
  .company__acn {
    font-size: 16px;
    color: var(--white);
  }
  .company__acn .label { color: var(--orange); }
  .divider { display: block; margin: 14px auto; }
  .contact__icons {
    display: flex; justify-content: center; gap: 8px;
    margin-bottom: 8px;
  }
  .contact__line {
    font-size: 16px;
    color: var(--white);
    line-height: 1.45;
  }
  .front__slogan {
    position: absolute;
    left: 0; right: 0; bottom: 0;
    height: 48px;
    background: var(--orange);
    color: var(--white);
    font-size: 15px;
    font-weight: 500;
    letter-spacing: .3px;
    display: flex; align-items: center; justify-content: center;
  }

  .back__brand {
    position: absolute;
    inset: 0;
    display: flex; align-items: center; justify-content: center;
    font-family: "Orbitron", "Montserrat", sans-serif;
    font-weight: 600;
    font-size: 38px;
    color: var(--orange);
    letter-spacing: 1px;
  }
</style>
</head>
<body>

  <section class="card card--front">
    <h1 class="front__company">KT Crewing Pty Ltd</h1>

    <div class="front__details">
      <p class="person__name">MICK HARLOW</p>
      <p class="person__role">DIRECTOR</p>
      <div class="person__dash"></div>
      <p class="company__acn"><span class="label">ACN</span>: 517 238 649</p>

      <svg class="divider" width="300" height="8" viewBox="0 0 300 8">
        <defs>
          <linearGradient id="lineFade" x1="0" x2="1">
            <stop offset="0" stop-color="#F15A29" stop-opacity="0"/>
            <stop offset=".5" stop-color="#F15A29"/>
            <stop offset="1" stop-color="#F15A29" stop-opacity="0"/>
          </linearGradient>
        </defs>
        <rect x="0" y="3" width="300" height="1.5" fill="url(#lineFade)"/>
      </svg>

      <div class="contact__icons">
        <svg width="18" height="18" viewBox="0 0 18 18" aria-label="phone">
          <circle cx="9" cy="9" r="8" fill="none" stroke="#F15A29" stroke-width="1.4"/>
          <path d="M6.2 5.2l1.4-.3.8 1.9-.9.7c.5 1.1 1.3 1.9 2.4 2.4l.7-.9 1.9.8-.3 1.4c-3.2.2-6.2-2.8-6-6z" fill="#F15A29"/>
        </svg>
        <svg width="18" height="18" viewBox="0 0 18 18" aria-label="email">
          <circle cx="9" cy="9" r="8" fill="none" stroke="#F15A29" stroke-width="1.4"/>
          <rect x="5" y="6" width="8" height="6" fill="none" stroke="#F15A29" stroke-width="1.2"/>
          <path d="M5 6l4 3.2L13 6" fill="none" stroke="#F15A29" stroke-width="1.2"/>
        </svg>
      </div>

      <p class="contact__line">0431 556 208</p>
      <p class="contact__line">mick@ktcrewing.com.au</p>

      <svg class="divider" width="300" height="8" viewBox="0 0 300 8">
        <rect x="0" y="3" width="300" height="1.5" fill="url(#lineFade)"/>
      </svg>
    </div>

    <p class="front__slogan">ONSITE AUTO ELECTRICIAN LABOUR HIRE</p>
  </section>

  <section class="card card--back">
    <p class="back__brand">KT Crewing</p>
  </section>

</body>
</html>
```